Memento Mori Calendar

I’m looking for a graphic designer to create a Memento Mori–style life calendar that captures the essence of OLVENTRA — minimal, timeless, and deeply philosophical.

The design should be black and white only, with a refined, clean aesthetic and a sense of stillness and precision.
It should feel modern yet eternal, reflecting the themes of time, mortality, and presence.

Deliverables (Print-Ready Files):

24 x 30 in

24 x 32 in

24 x 36 in

A1 (594 x 841 mm)

All formats should be high-resolution and ready for professional printing (300 DPI, CMYK).

Design Requirements:

The calendar layout should follow the Memento Mori life calendar concept (weeks of life represented as small squares or circles).

The overall tone: minimal, meditative, monochrome.

Include the brand name: OLVENTRA (in an elegant, understated placement).

Add the following quote at the bottom or in a subtle position:

“Life can only be understood backwards; but it must be lived forwards.”
— Henrik Vastmoe

Target Market(s)

The OLVENTRA audience consists of urban, creative individuals aged 25 to 45, belonging to a middle to upper-middle income class. They lead conscious, quietly ambitious lives, seeking balance between inner depth and modern design. Their values center on awareness, presence, authenticity, and emotional depth, reflected in their preference for a monochrome, minimal, and timeless aesthetic. They tend to be introverted, reflective, and spiritually curious, drawn to brands that embody meaning and restraint rather than excess. Their cultural and stylistic affinities include Pyrel, Tulve, Ni Ostra, The Quiet Bench Guild, Durvanne, and Ombrix — labels that share OLVENTRAs devotion to simplicity, substance, and subtle ritual.

Font styles to use
Serif
Sans Serif

Colors

Designer to choose only greyscale colors for use in the design.

Requirements
Must have
• The calendar layout should follow the Memento Mori life calendar concept (weeks of life represented as small squares or circles). The overall tone: minimal, meditative, monochrome. Include the brand name: qrnvalto (in an elegant, understated placement). Add the following quote at the bottom or in a subtle position: “Life can only be understood backwards; but it must be lived forwards.” — Henrik Vastmoe

```html
<!DOCTYPE html>
<html lang="en">
<head>
<meta charset="utf-8">
<title>Memento Mori Life Calendar – QRNVALTO</title>
<link rel="stylesheet" href="https://fonts.googleapis.com/css2?family=Archivo+Black&family=Crimson+Pro:ital,wght@1,400;1,700&family=Montserrat:wght@500;600&family=Playfair+Display:wght@500&display=swap">
<style>
  :root {
    --ink: #111111;
    --frame: #333333;
    --rule: #999999;
    --muted: #8f8f8f;
    --paper: #ffffff;
    --box: #262626;
  }
  html, body {
    margin: 0;
    padding: 0;
    width: 907px;
    height: 1200px;
    overflow: hidden;
    background: var(--paper);
  }
  .poster { display: block; width: 907px; height: 1200px; }
  .outer-frame { fill: none; stroke: var(--frame); stroke-width: 3.5; }
  .inner-frame { fill: none; stroke: var(--rule); stroke-width: 4; stroke-linecap: round; }
  .brand-tab { fill: var(--ink); }
  .brand-name {
    font-family: "Archivo Black", sans-serif;
    font-size: 44px;
    fill: var(--paper);
    letter-spacing: 1px;
  }
  .week-box { fill: none; stroke: var(--box); stroke-width: 0.8; }
  .week-label, .year-label {
    font-family: "Montserrat", sans-serif;
    font-weight: 500;
    fill: var(--ink);
  }
  .week-label { font-size: 4.6px; text-anchor: middle; }
  .week-label.major { font-size: 9px; font-weight: 600; }
  .year-label { font-size: 4.6px; text-anchor: end; dominant-baseline: central; }
  .year-label.decade { font-size: 9px; fill: var(--muted); }
  .title-vertical {
    font-family: "Playfair Display", serif;
    font-weight: 500;
    font-size: 66px;
    fill: var(--ink);
  }
  .divider { fill: var(--rule); }
  .quote {
    font-family: "Crimson Pro", serif;
    font-style: italic;
    font-size: 16px;
    fill: #444444;
    text-anchor: middle;
  }
  .quote-author {
    font-family: "Crimson Pro", serif;
    font-style: italic;
    font-weight: 700;
    font-size: 16px;
    fill: #333333;
    text-anchor: middle;
  }
</style>
</head>
<body>
<svg class="poster" viewBox="0 0 907 1200" xmlns="http://www.w3.org/2000/svg" role="img" aria-label="Memento Mori life calendar: 80 years of 52 weeks">
  <defs>
    <pattern id="week-grid" width="10.7" height="10.7" patternUnits="userSpaceOnUse">
      <rect class="week-box" x="1.6" y="1.6" width="7.4" height="7.4" rx="1.8"/>
    </pattern>
    <rect id="decade-block" width="278.2" height="107" fill="url(#week-grid)"/>
  </defs>

  <!-- frames -->
  <rect class="outer-frame" x="79" y="79" width="754" height="1047" rx="14"/>
  <path class="inner-frame" d="M628 94 H809 Q819 94 819 104 V1102 Q819 1112 809 1112 H530 M372 1112 H103 Q93 1112 93 1102 V104 Q93 94 103 94 H283"/>

  <!-- brand tab -->
  <path class="brand-tab" d="M293 79 H618 V137 Q618 143 612 143 H299 Q293 143 293 137 Z"/>
  <text class="brand-name" x="455.5" y="127" text-anchor="middle">QRNVALTO</text>

  <!-- week headers -->
  <g class="week-headers">
    <text class="week-label" x="153" y="165">1</text>
    <text class="week-label" x="163.7" y="165">2</text>
    <text class="week-label" x="174.4" y="165">3</text>
    <text class="week-label" x="185.1" y="165">4</text>
    <text class="week-label major" x="195.8" y="166">5</text>
    <text class="week-label" x="206.5" y="165">6</text>
    <text class="week-label" x="217.2" y="165">7</text>
    <text class="week-label" x="227.9" y="165">8</text>
    <text class="week-label" x="238.6" y="165">9</text>
    <text class="week-label major" x="249.3" y="166">10</text>
    <text class="week-label" x="260" y="165">11</text>
    <text class="week-label" x="270.7" y="165">12</text>
    <text class="week-label" x="281.4" y="165">13</text>
    <text class="week-label" x="292.1" y="165">14</text>
    <text class="week-label major" x="302.8" y="166">15</text>
    <text class="week-label" x="313.5" y="165">16</text>
    <text class="week-label" x="324.2" y="165">17</text>
    <text class="week-label" x="334.9" y="165">18</text>
    <text class="week-label" x="345.6" y="165">19</text>
    <text class="week-label major" x="356.3" y="166">20</text>
    <text class="week-label" x="367" y="165">21</text>
    <text class="week-label" x="377.7" y="165">22</text>
    <text class="week-label" x="388.4" y="165">23</text>
    <text class="week-label" x="399.1" y="165">24</text>
    <text class="week-label major" x="409.8" y="166">25</text>
    <text class="week-label" x="420.5" y="165">26</text>

    <text class="week-label" x="511.15" y="165">27</text>
    <text class="week-label" x="521.85" y="165">28</text>
    <text class="week-label" x="532.55" y="165">29</text>
    <text class="week-label major" x="543.25" y="166">30</text>
    <text class="week-label" x="553.95" y="165">31</text>
    <text class="week-label" x="564.65" y="165">32</text>
    <text class="week-label" x="575.35" y="165">33</text>
    <text class="week-label" x="586.05" y="165">34</text>
    <text class="week-label major" x="596.75" y="166">35</text>
    <text class="week-label" x="607.45" y="165">36</text>
    <text class="week-label" x="618.15" y="165">37</text>
    <text class="week-label" x="628.85" y="165">38</text>
    <text class="week-label" x="639.55" y="165">39</text>
    <text class="week-label major" x="650.25" y="166">40</text>
    <text class="week-label" x="660.95" y="165">41</text>
    <text class="week-label" x="671.65" y="165">42</text>
    <text class="week-label" x="682.35" y="165">43</text>
    <text class="week-label" x="693.05" y="165">44</text>
    <text class="week-label major" x="703.75" y="166">45</text>
    <text class="week-label" x="714.45" y="165">46</text>
    <text class="week-label" x="725.15" y="165">47</text>
    <text class="week-label" x="735.85" y="165">48</text>
    <text class="week-label" x="746.55" y="165">49</text>
    <text class="week-label major" x="757.25" y="166">50</text>
    <text class="week-label" x="767.95" y="165">51</text>
    <text class="week-label" x="778.65" y="165">52</text>
  </g>

  <!-- week grids: 8 decades, two halves -->
  <g class="weeks-first-half">
    <use href="#decade-block" x="147.7" y="170"/>
    <use href="#decade-block" x="147.7" y="283.9"/>
    <use href="#decade-block" x="147.7" y="397.8"/>
    <use href="#decade-block" x="147.7" y="511.7"/>
    <use href="#decade-block" x="147.7" y="625.6"/>
    <use href="#decade-block" x="147.7" y="739.5"/>
    <use href="#decade-block" x="147.7" y="853.4"/>
    <use href="#decade-block" x="147.7" y="967.3"/>
  </g>
  <g class="weeks-second-half">
    <use href="#decade-block" x="505.8" y="170"/>
    <use href="#decade-block" x="505.8" y="283.9"/>
    <use href="#decade-block" x="505.8" y="397.8"/>
    <use href="#decade-block" x="505.8" y="511.7"/>
    <use href="#decade-block" x="505.8" y="625.6"/>
    <use href="#decade-block" x="505.8" y="739.5"/>
    <use href="#decade-block" x="505.8" y="853.4"/>
    <use href="#decade-block" x="505.8" y="967.3"/>
  </g>

  <!-- year labels -->
  <g class="year-labels">
    <g transform="translate(0,170)">
      <text class="year-label" x="143" y="5.35">1</text><text class="year-label" x="143" y="16.05">2</text><text class="year-label" x="143" y="26.75">3</text><text class="year-label" x="143" y="37.45">4</text><text class="year-label" x="143" y="48.15">5</text><text class="year-label" x="143" y="58.85">6</text><text class="year-label" x="143" y="69.55">7</text><text class="year-label" x="143" y="80.25">8</text><text class="year-label" x="143" y="90.95">9</text><text class="year-label decade" x="143.5" y="101.65">10</text>
    </g>
    <g transform="translate(0,283.9)">
      <text class="year-label" x="143" y="5.35">11</text><text class="year-label" x="143" y="16.05">12</text><text class="year-label" x="143" y="26.75">13</text><text class="year-label" x="143" y="37.45">14</text><text class="year-label" x="143" y="48.15">15</text><text class="year-label" x="143" y="58.85">16</text><text class="year-label" x="143" y="69.55">17</text><text class="year-label" x="143" y="80.25">18</text><text class="year-label" x="143" y="90.95">19</text><text class="year-label decade" x="143.5" y="101.65">20</text>
    </g>
    <g transform="translate(0,397.8)">
      <text class="year-label" x="143" y="5.35">21</text><text class="year-label" x="143" y="16.05">22</text><text class="year-label" x="143" y="26.75">23</text><text class="year-label" x="143" y="37.45">24</text><text class="year-label" x="143" y="48.15">25</text><text class="year-label" x="143" y="58.85">26</text><text class="year-label" x="143" y="69.55">27</text><text class="year-label" x="143" y="80.25">28</text><text class="year-label" x="143" y="90.95">29</text><text class="year-label decade" x="143.5" y="101.65">30</text>
    </g>
    <g transform="translate(0,511.7)">
      <text class="year-label" x="143" y="5.35">31</text><text class="year-label" x="143" y="16.05">32</text><text class="year-label" x="143" y="26.75">33</text><text class="year-label" x="143" y="37.45">34</text><text class="year-label" x="143" y="48.15">35</text><text class="year-label" x="143" y="58.85">36</text><text class="year-label" x="143" y="69.55">37</text><text class="year-label" x="143" y="80.25">38</text><text class="year-label" x="143" y="90.95">39</text><text class="year-label decade" x="143.5" y="101.65">40</text>
    </g>
    <g transform="translate(0,625.6)">
      <text class="year-label" x="143" y="5.35">41</text><text class="year-label" x="143" y="16.05">42</text><text class="year-label" x="143" y="26.75">43</text><text class="year-label" x="143" y="37.45">44</text><text class="year-label" x="143" y="48.15">45</text><text class="year-label" x="143" y="58.85">46</text><text class="year-label" x="143" y="69.55">47</text><text class="year-label" x="143" y="80.25">48</text><text class="year-label" x="143" y="90.95">49</text><text class="year-label decade" x="143.5" y="101.65">50</text>
    </g>
    <g transform="translate(0,739.5)">
      <text class="year-label" x="143" y="5.35">51</text><text class="year-label" x="143" y="16.05">52</text><text class="year-label" x="143" y="26.75">53</text><text class="year-label" x="143" y="37.45">54</text><text class="year-label" x="143" y="48.15">55</text><text class="year-label" x="143" y="58.85">56</text><text class="year-label" x="143" y="69.55">57</text><text class="year-label" x="143" y="80.25">58</text><text class="year-label" x="143" y="90.95">59</text><text class="year-label decade" x="143.5" y="101.65">60</text>
    </g>
    <g transform="translate(0,853.4)">
      <text class="year-label" x="143" y="5.35">61</text><text class="year-label" x="143" y="16.05">62</text><text class="year-label" x="143" y="26.75">63</text><text class="year-label" x="143" y="37.45">64</text><text class="year-label" x="143" y="48.15">65</text><text class="year-label" x="143" y="58.85">66</text><text class="year-label" x="143" y="69.55">67</text><text class="year-label" x="143" y="80.25">68</text><text class="year-label" x="143" y="90.95">69</text><text class="year-label decade" x="143.5" y="101.65">70</text>
    </g>
    <g transform="translate(0,967.3)">
      <text class="year-label" x="143" y="5.35">71</text><text class="year-label" x="143" y="16.05">72</text><text class="year-label" x="143" y="26.75">73</text><text class="year-label" x="143" y="37.45">74</text><text class="year-label" x="143" y="48.15">75</text><text class="year-label" x="143" y="58.85">76</text><text class="year-label" x="143" y="69.55">77</text><text class="year-label" x="143" y="80.25">78</text><text class="year-label" x="143" y="90.95">79</text><text class="year-label decade" x="143.5" y="101.65">80</text>
    </g>
  </g>

  <!-- central title with tapered dividers -->
  <polygon class="divider" points="463,172 464.3,240 464,333 462,333 461.7,240"/>
  <polygon class="divider" points="462,910 464,910 464.3,1000 463,1070 461.7,1000"/>
  <text class="title-vertical" transform="translate(487,621) rotate(-90)" text-anchor="middle" textLength="554" lengthAdjust="spacingAndGlyphs">MOMENTO MORI</text>

  <!-- quote -->
  <text class="quote" x="455" y="1093">“Life can only be understood backwards; but it must be lived forwards.”</text>
  <text class="quote-author" x="451" y="1114">Henrik Vastmoe</text>
</svg>
</body>
</html>
```